Criação de Papelaria Profissional para Beleza
A empresa queria:
" Atendemos clientes adultos masculino, feminino, adolescentes para tratamentos estéticos diversos como acne, rejuvenescimento facial, redução de medidas faciais e corporais, depilação, tratamento de celulite, estrias, medicina capilar, laser, cicatrizes, manchas, melasma, pequenos vasos, poros dilatados, limpeza de pele "

```html
<!DOCTYPE html>
<html lang="pt-BR">
<head>
<meta charset="UTF-8">
<title>Lumera Clínica Estética — Papel Timbrado</title>
<link href="https://fonts.googleapis.com/css2?family=Montserrat:wght@400;500;600&display=swap" rel="stylesheet">
<style>
  :root {
    --backdrop: #c9c9c9;
    --paper: #ffffff;
    --teal: #2aa8a0;
    --teal-deep: #124f57;
    --ink: #3a3a3a;
    --signature-tone: #d9d9d9;
  }
  * { margin: 0; padding: 0; box-sizing: border-box; }
  html, body {
    width: 1200px;
    height: 1200px;
    overflow: hidden;
    background: var(--backdrop);
    font-family: "Montserrat", sans-serif;
  }
  .letterhead {
    position: absolute;
    left: 233px;
    top: 67px;
    width: 734px;
    height: 1061px;
    background: var(--paper);
    box-shadow: 0 6px 18px rgba(0, 0, 0, 0.18);
  }
  .brand {
    position: absolute;
    left: 60px;
    top: 44px;
    display: flex;
    align-items: center;
    gap: 14px;
    color: var(--teal-deep);
    font-weight: 600;
  }
  .brand-dot {
    width: 38px;
    height: 38px;
    border-radius: 50%;
    background: var(--teal-deep);
  }
  .brand-name {
    font-size: 40px;
    line-height: 1;
    letter-spacing: 1px;
  }
  .brand-tagline {
    font-size: 13px;
    letter-spacing: 3px;
    margin-top: 6px;
  }
  .contact {
    position: absolute;
    top: 978px;
    display: flex;
    align-items: center;
    gap: 10px;
    font-size: 12px;
    color: var(--ink);
    line-height: 1.35;
  }
  .contact-phone { left: 24px; }
  .contact-address { left: 178px; }
  .contact-icon {
    width: 28px;
    height: 28px;
    border-radius: 6px;
    background: var(--teal);
    display: flex;
    align-items: center;
    justify-content: center;
    flex-shrink: 0;
  }
  .signature {
    position: absolute;
    left: 500px;
    top: 950px;
    width: 130px;
    height: 40px;
    background: var(--signature-tone);
    border-radius: 4px;
  }
  .signer {
    position: absolute;
    left: 500px;
    top: 1000px;
    font-size: 14px;
    color: var(--ink);
  }
  .footer-band {
    position: absolute;
    left: 0;
    bottom: 0;
    width: 100%;
    height: 22px;
    background: var(--teal);
  }
</style>
</head>
<body>
  <main class="letterhead">
    <header class="brand">
      <span class="brand-dot"></span>
      <div>
        <div class="brand-name">LUMERA</div>
        <div class="brand-tagline">CLÍNICA ESTÉTICA</div>
      </div>
    </header>

    <div class="contact contact-phone">
      <span class="contact-icon">
        <svg width="16" height="16" viewBox="0 0 24 24" aria-hidden="true">
          <path fill="#fff" d="M6.6 10.8a15.1 15.1 0 0 0 6.6 6.6l2.2-2.2c.3-.3.7-.4 1-.2 1.1.4 2.3.6 3.6.6.6 0 1 .4 1 1V20c0 .6-.4 1-1 1A17 17 0 0 1 3 4c0-.6.4-1 1-1h3.5c.6 0 1 .4 1 1 0 1.3.2 2.5.6 3.6.1.3 0 .7-.2 1z"/>
        </svg>
      </span>
      <span>(11) 98412-3370</span>
    </div>

    <div class="contact contact-address">
      <span class="contact-icon">
        <svg width="16" height="16" viewBox="0 0 24 24" aria-hidden="true">
          <path fill="#fff" d="M12 2a7 7 0 0 0-7 7c0 5.3 7 13 7 13s7-7.7 7-13a7 7 0 0 0-7-7zm0 9.5A2.5 2.5 0 1 1 12 6.5a2.5 2.5 0 0 1 0 5z"/>
        </svg>
      </span>
      <span>Rua das Acácias 214,<br>Vila Mariana, São Paulo</span>
    </div>

    <div class="signature" role="img" aria-label="Assinatura manuscrita da cofundadora"></div>
    <div class="signer">Name, co-founder</div>

    <div class="footer-band"></div>
  </main>
</body>
</html>
```